MeadowLantern.com

Updated Website Structure for MeadowLantern.com
1. Home Page

(Add social media links in footer or sidebar)
Suggested addition:

Stay Connected
Follow Meadow Lantern for daily encouragement, calming tools, and community stories.

[Facebook Icon] [Instagram Icon] [YouTube Icon]
@MeadowLanternHome

2. How It Works

(No major change — keep focused on process and trust building)

3. Ebook Store

(Add social links at the bottom of the page)

Want more free content?
Follow us on social media for sneak peeks, affirmations, and updates on new releases!

[Facebook] [Instagram] [YouTube]

4. Certification Page

(Optional social proof addition)

Connect with Certified Meadow Lanterns
Join our online community and see real stories of growth and courage.

Follow us on social media to see how others are supporting each other:

5. Membership Tiers

(Keep page simple, but can include icons in footer)

6. About Me

Suggested addition:

Let’s Stay Connected
I love hearing from others walking this path.

Facebook: @MeadowLanternHome

Instagram: @MeadowLanternHome

YouTube: Meadow Lantern Channel

7. Disclosure Page

(Keep links in footer only for professional feel.)

8. Global Footer (Site-wide)

Every page should include a calming footer with:

Navigation links (Home | About Me | How It Works | Ebook Store | Certification | Membership | Disclosure)

Social media icons

Copyright info

Example footer text:

🌿 Walking with fear, choosing courage, calming the nervous system together.

© 2025 MeadowLantern.com | All rights reserved

```html
<!DOCTYPE html>
<html lang="en">
<head>
<meta charset="utf-8">
<title>Meadow Lantern — Site Screens</title>
<link href="https://fonts.googleapis.com/css2?family=Poppins:wght@500;600;700&family=Lato:wght@400;700&family=Playfair+Display:ital@1&display=swap" rel="stylesheet">
<style>
:root{
  --stage:#322838;
  --ink:#2a1230;
  --body:#3a2840;
  --accent:#85719a;
  --lilac:#e9c3e4;
  --pink:#ecb6d3;
  --card:#f3d2e6;
  --card-edge:#f7e0ee;
  --hero-a:#eeb8d6;
  --hero-b:#ecc4e3;
  --pill:#f1d3ea;
}
*{box-sizing:border-box;margin:0;padding:0}
html,body{width:1200px;height:1200px;overflow:hidden;background:var(--stage)}
body{position:relative;font-family:'Lato',sans-serif;color:var(--body)}
.screen{position:absolute;width:326px;overflow:hidden}
h2,h3,h4,.btn,.nav{font-family:'Poppins',sans-serif}
.icon{fill:var(--accent)}
.icon-dark{fill:var(--ink)}

/* Home */
.home{left:58px;top:66px;height:221px;background:linear-gradient(135deg,var(--hero-a),var(--hero-b))}
.nav{height:17px;background:#f6dcec;display:flex;align-items:center;font-size:5.2px;font-weight:500;color:var(--ink);padding-left:6px;gap:0}
.nav span{display:flex;align-items:center;gap:2px;margin-right:9px}
.nav svg{width:5px;height:5px}
.toggle{margin-left:auto;margin-right:6px;width:18px;height:8px;border-radius:4px;background:#fbeff6;position:relative}
.toggle::before{content:"";position:absolute;left:1px;top:1px;width:6px;height:6px;border-radius:50%;background:var(--ink)}
.hero-art{position:absolute;left:85px;top:25px;width:155px;height:134px;border-radius:7px;background:radial-gradient(circle at 50% 50%,#f1c6e4 0 34%,#86729b 36%)}
.hero-title{position:absolute;top:171px;width:100%;text-align:center;font-size:16px;font-weight:700;color:var(--ink)}
.hero-sub{position:absolute;top:201px;left:38px;width:250px;text-align:center;font-size:6px;line-height:9.5px;color:var(--ink)}

/* Long page */
.pages{left:431px;top:66px;width:324px;height:1087px}
.sec{position:relative;text-align:center}
.sec h2{font-size:9px;font-weight:500;color:var(--ink);padding-top:9px}
.lead{font-size:4.8px;margin-top:6px;color:var(--ink)}
.lilac{background:var(--lilac)}
.pink{background:var(--pink)}
.card{position:absolute;background:var(--card);border:1px solid var(--card-edge);border-radius:5px;box-shadow:0 1px 4px rgba(150,80,130,.15);text-align:center;padding:0 6px}
.card h3{font-size:5.4px;font-weight:500;color:var(--ink)}
.card p{font-size:4.7px;line-height:8px;color:var(--body)}
.btn{display:inline-block;background:var(--accent);color:#fff;font-size:4.4px;font-weight:600;border-radius:8px;padding:4px 8px}
.how{height:271px}
.how .card{width:99px;height:92px;padding-top:13px}
.how .card svg{width:18px;height:16px}
.how .card h3{margin:6px 0 6px}
.ebook{height:324px}
.ebook .card{width:87px;height:110px;padding-top:12px}
.ebook .card svg{width:19px;height:19px}
.ebook .card h3{margin:6px 0 6px}
.ebook .card .btn{margin-top:7px}
.cert{height:174px}
.cert .badge{position:absolute;left:76px;top:86px;width:22px;height:30px}
.cert-copy{position:absolute;left:164px;top:44px;width:138px;text-align:left;font-size:4.8px;line-height:8.1px;color:var(--ink)}
.cert-copy p{margin-bottom:6.5px}
.cert-copy .btn{margin-top:1px;padding:4px 8px}
.tiers{height:318px}
.tier{top:71px;width:89px;height:204px;padding-top:14px}
.tier svg{width:12px;height:12px}
.tier h3{margin:6px 0 6px;font-weight:600}
.price{font-size:9px;color:var(--accent);margin:13px 0 14px}
.tier ul{list-style:none;text-align:left;font-size:4.4px;line-height:6.4px;padding:0 3px}
.tier li{position:relative;padding-left:7px;margin-bottom:4.6px}
.tier li::before{content:"✓";position:absolute;left:0;color:var(--accent)}
.tier .btn{margin-top:5px}
.ghost{background:transparent;color:var(--accent);border:0.8px solid var(--accent)}

/* About + Disclosure */
.about{left:812px;top:66px;width:324px;height:595px;background:linear-gradient(180deg,var(--pink),#eec8e6);}
.about h2{position:absolute;top:15px;width:100%;text-align:center;font-size:9.6px;font-weight:500;color:var(--ink)}
.portrait{position:absolute;left:15px;top:37px;width:139px;height:139px;border-radius:6px;background:linear-gradient(160deg,#e8e2e0,#c84a4a 70%,#a8222a)}
.about-copy{position:absolute;left:163px;top:34px;width:143px;font-size:4.8px;line-height:8.1px;color:var(--ink)}
.about-copy p{margin-bottom:7px}
.about-copy .btn{background:var(--pill);color:var(--ink);margin-top:0;padding:4px 8px}
.disclosure{position:absolute;left:43px;top:227px;width:240px;color:var(--ink)}
.disclosure h2{position:static;text-align:left;font-size:9px;padding:0}
.disclosure h4{font-size:5.4px;font-weight:600;margin-bottom:5px}
.disclosure p{font-size:4.8px;line-height:8.1px;margin-bottom:7px}
.disclosure .intro{margin-top:7px;margin-bottom:8px}
.footer{position:absolute;top:499px;width:100%;text-align:center}
.brand{display:inline-flex;align-items:center;gap:4px;font-family:'Poppins',sans-serif;font-weight:600;font-size:8.2px;color:var(--accent)}
.brand i{width:7px;height:7px;border-radius:50%;background:var(--accent)}
.tagline{font-family:'Playfair Display',serif;font-style:italic;font-size:5px;color:var(--body);margin-top:9px}
.socials{display:flex;justify-content:center;gap:9.3px;margin-top:10px}
.socials span{width:11px;height:11px;border-radius:50%;background:var(--accent)}
.foot-links{display:flex;justify-content:center;gap:6px;font-size:4.6px;margin-top:7px;color:var(--ink)}
.copyright{font-size:4px;margin-top:10px;color:var(--ink)}
</style>
</head>
<body>

<section class="screen home">
  <nav class="nav">
    <span>✕</span>
    <span><svg viewBox="0 0 10 10" class="icon-dark"><path d="M5 1 1 5h1.5v4h2V7h1v2h2V5H9z"/></svg>Home</span>
    <span><svg viewBox="0 0 10 10" class="icon-dark"><circle cx="3" cy="4" r="2"/><circle cx="7" cy="6" r="2"/></svg>How It Works</span>
    <span><svg viewBox="0 0 10 10" class="icon-dark"><rect x="2" y="1" width="6" height="8" rx="1"/></svg>Ebooks</span>
    <span><svg viewBox="0 0 10 10" class="icon-dark"><circle cx="5" cy="4" r="3"/><path d="M3 6 2 9l3-1 3 1-1-3z"/></svg>Certification</span>
    <span><svg viewBox="0 0 10 10" class="icon-dark"><circle cx="3" cy="3" r="1.6"/><circle cx="7" cy="3" r="1.6"/><path d="M0 8a3 3 0 0 1 6 0zM4 8a3 3 0 0 1 6 0z"/></svg>Membership</span>
    <span><svg viewBox="0 0 10 10" class="icon-dark"><circle cx="5" cy="3" r="2.2"/><path d="M1 10a4 4 0 0 1 8 0z"/></svg>About</span>
    <span><svg viewBox="0 0 10 10" class="icon-dark"><path d="M2 1h4l2 2v6H2z"/></svg>Disclosure</span>
    <div class="toggle"></div>
  </nav>
  <div class="hero-art" role="img" aria-label="Heart-shaped emblem with two women holding hands"></div>
  <h2 class="hero-title">Welcome to Meadow Lantern</h2>
  <p class="hero-sub">Walking with fear. Choosing courage. Your space for calm, community, and courage through anxiety.</p>
</section>

<section class="screen pages">
  <div class="sec how lilac">
    <h2>How It Works</h2>
    <p class="lead">Discover the process of building trust and finding calm. Step-by-step guidance to help you on your journey.</p>
    <div class="card" style="left:56px;top:55px">
      <svg viewBox="0 0 20 18" class="icon-dark"><circle cx="8" cy="5" r="4"/><path d="M1 18a7 7 0 0 1 14 0z"/><path d="M15 5h2V3h1.4v2h2v1.4h-2v2H17v-2h-2z"/></svg>
      <h3>Join Our Community</h3><p>Sign up and become part of our supportive network of individuals on similar journeys.</p></div>
    <div class="card" style="left:164px;top:55px">
      <svg viewBox="0 0 20 18" class="icon-dark"><path d="M1 2c3-1 6-1 8 1v14c-2-2-5-2-8-1zM19 2c-3-1-6-1-8 1v14c2-2 5-2 8-1z"/></svg>
      <h3>Access Resources</h3><p>Explore our library of ebooks, guides, and tools designed to help you manage anxiety.</p></div>
    <div class="card" style="left:56px;top:156px">
      <svg viewBox="0 0 20 18" class="icon-dark"><path d="M2 9l5-5h5l4 3-3 3-3-2-5 6z"/><path d="M18 9l-5 5H8l4-4z"/></svg>
      <h3>Connect with Partners</h3><p>Find certified Meadow Lanterns who can provide guidance, support, and understanding.</p></div>
    <div class="card" style="left:164px;top:156px">
      <svg viewBox="0 0 20 18" class="icon-dark"><path d="M10 17 2 9a4.5 4.5 0 0 1 8-5 4.5 4.5 0 0 1 8 5z"/></svg>
      <h3>Grow Together</h3><p>Participate in community events and activities that promote healing and connection.</p></div>
  </div>

  <div class="sec ebook pink">
    <h2 style="padding-top:22px">Ebook Store</h2>
    <p class="lead">Explore our collection of helpful ebooks to support your journey.</p>
    <div class="card" style="left:68px;top:71px">
      <svg viewBox="0 0 20 20" class="icon"><path d="M9 2C5 2 3 5 3 8c-2 2-2 6 1 8 1 2 3 3 5 2zM11 2c4 0 6 3 6 6 2 2 2 6-1 8-1 2-3 3-5 2z"/></svg>
      <h3>Understanding Anxiety</h3><p>A comprehensive guide to recognizing and understanding anxiety patterns.</p>
      <span class="btn">Get This Ebook</span></div>
    <div class="card" style="left:164px;top:71px">
      <svg viewBox="0 0 20 20" class="icon"><path d="M3 1 1 3l7 7-6 6 2 2 6-6 6 6 2-2-6-6 4-4a3 3 0 0 0 3-4l-2 2-2-2 2-2a3 3 0 0 0-4 3l-4 4z"/></svg>
      <h3>Coping Strategies</h3><p>Practical techniques to manage anxiety in daily life.</p>
      <span class="btn">Get This Ebook</span></div>
    <div class="card" style="left:68px;top:191px">
      <svg viewBox="0 0 20 20" class="icon"><path d="M10 1 2 4v6c0 5 4 8 8 9 4-1 8-4 8-9V4zm0 3v13c-3-1-5-4-5-7V6z"/></svg>
      <h3>Building Resilience</h3><p>Learn how to develop mental and emotional strength to face challenges.</p>
      <span class="btn">Get This Ebook</span></div>
  </div>

  <div class="sec cert lilac">
    <h2 style="padding-top:22px">Certification</h2>
    <svg class="badge icon" viewBox="0 0 22 30"><circle cx="11" cy="11" r="10"/><circle cx="11" cy="11" r="4.5" fill="#e9c3e4"/><path d="M4 18 1 27l4-1 2 3 3-8zM18 18l3 9-4-1-2 3-3-8z"/></svg>
    <div class="cert-copy">
      <p>Connect with Certified Meadow Lanterns and join our community of growth and courage.</p>
      <p>Our certification program ensures that all Meadow Lanterns have completed comprehensive training in anxiety support techniques, active listening, and creating safe spaces for healing conversations.</p>
      <p>Whether you're looking for support or interested in becoming a certified Meadow Lantern yourself, we're here to help you on your journey.</p>
      <span class="btn">Become Certified</span>
    </div>
  </div>

  <div class="sec tiers pink">
    <h2 style="padding-top:22px">Membership Tiers</h2>
    <p class="lead">Choose the membership level that best supports your needs and enjoy exclusive benefits.</p>
    <div class="card tier" style="left:16px">
      <svg viewBox="0 0 12 12" class="icon"><path d="M5.4 12V6C3 6 1 4.5 1 2c2.5 0 4.4 1.5 4.6 3.5C6 3 8 1 11 1c0 3-2 5-4.6 5v6z"/></svg>
      <h3>Basic</h3><p>For those beginning their journey</p>
      <div class="price">Free</div>
      <ul><li>Access to community forum</li><li>Weekly newsletter</li><li>Basic anxiety management resources</li></ul>
      <span class="btn ghost">Join Now</span></div>
    <div class="card tier" style="left:118px">
      <svg viewBox="0 0 12 12" class="icon"><path d="M1 11c1-4 4-8 10-9 0 5-3 8-7 8-1 0-2 0-3 1z"/></svg>
      <h3>Partner</h3><p>Our most popular option</p>
      <div class="price" style="margin:13px 0 12px">$19/month</div>
      <ul><li>All Basic features</li><li>Access to all ebooks</li><li>Monthly group sessions</li><li>Priority forum support</li><li>Discounts on one-on-one sessions</li></ul>
      <span class="btn">Join Now</span></div>
    <div class="card tier" style="left:219px">
      <svg viewBox="0 0 12 12" class="icon"><path d="M6 0 9 4H7.5L10 7H8l3 3H7v2H5v-2H1l3-3H2l2.5-3H3z"/></svg>
      <h3>Premium</h3><p>Complete support package</p>
      <div class="price" style="margin:13px 0 12px">$39/month</div>
      <ul><li>All Partner features</li><li>Two one-on-one sessions monthly</li><li>Personalized anxiety management plan</li><li>24/7 crisis chat support</li><li>Early access to new resources</li></ul>
      <span class="btn">Join Now</span></div>
  </div>
</section>

<section class="screen about">
  <h2>About Me</h2>
  <div class="portrait" role="img" aria-label="Portrait photo of the founder in red glasses and a red floral shirt"></div>
  <div class="about-copy">
    <p>I love hearing from others walking this path. Let's stay connected and support each other.</p>
    <p>My journey with anxiety began over a decade ago, and through my own struggles, I discovered the power of community and shared experiences. What started as personal coping mechanisms evolved into a passion for helping others navigate their anxiety journeys.</p>
    <p>Meadow Lantern was born from the belief that no one should face anxiety alone. We're building a community where vulnerability is strength, and support is always available.</p>
    <p>When I'm not working on Meadow Lantern, you can find me hiking, practicing mindfulness, or curled up with a good book and my two rescue cats.</p>
    <span class="btn">Get In Touch</span>
  </div>

  <div class="disclosure">
    <h2>Disclosure</h2>
    <p class="intro">Read our policies and understand our commitments.</p>
    <h4>Privacy Policy</h4>
    <p>Your privacy is important to us. We are committed to protecting your personal information and being transparent about what data we collect and how we use it.</p>
    <h4>Terms of Service</h4>
    <p>By using our services, you agree to our terms of service. These terms outline the rules and guidelines for using Meadow Lantern resources and community.</p>
    <h4>Disclaimer</h4>
    <p>Meadow Lantern provides supportive resources and community for anxiety management. We are not a substitute for professional medical advice, diagnosis, or treatment. Always seek the advice of your physician or other qualified health provider with any questions you may have regarding a medical condition.</p>
    <h4>Community Guidelines</h4>
    <p>Our community is built on respect, empathy, and support. We have zero tolerance for harassment, discrimination, or harmful behavior. All members are expected to adhere to our community guidelines.</p>
    <h4>Contact Information</h4>
    <p>If you have any questions about our policies, please contact us at privacy@meadowlantern.com.</p>
  </div>

  <footer class="footer">
    <div class="brand"><i></i>Meadow Lantern</div>
    <p class="tagline">Walking with fear, choosing courage, calming the nervous system together.</p>
    <div class="socials" aria-label="Social media links">
      <span></span><span></span><span></span><span></span><span></span><span></span><span></span><span></span><span></span><span></span>
    </div>
    <div class="foot-links"><span>Home</span><span>How It Works</span><span>Ebooks</span><span>Certification</span><span>Membership</span><span>About</span><span>Disclosure</span></div>
    <p class="copyright">© 2025 MeadowLantern.com. All rights reserved.</p>
  </footer>
</section>

</body>
</html>
```